Labels for Bees Wax Candles & Honey Jars

We need labels for jars of natural honey. Most of our jars are square and the labels about 2" by 2".

Also we make bees wax candles of various sizes. We wish to wrap th enables around the circular candles which are between 2" and 3" in diameter... thus another have inch per label so they can be attached adhesively. The candles also vary in height... therefor th enables need to be 1.5", 2" and 3" in height.

We ar elooking for a very artistic and simple label that may include vibrant colors.
The name of our company must be displayed.. Candles by Morrow and for the Honey.... Morrow's All Natural Honey
Updates

The labels will be used for both Honey Jars as well as Bees Wax candles. There will be various sizes but that is something that can be adjusted after the initial design is approved. The Honey Jars should read "Natural Honey by Morrow" and the Candle labels should read "Natural Bees Wax Candles by Morrow" I am interested in simple, colorful, legible, and arty labels that pertain to bees and the natural environment. Hope this helps. We may also use a similar design on our web page. The size of the label on the honey will be 2" by 2" and the candles will vary.

Target Market(s)

Individual that purchase natural and organic products.

Requirements
Must have
• Labels should be very creative but legible and the emphasis on the candles should be all natural bees wax and the emphasis on the honey should be all natural honey. We are talking about the same design but different sizes and names.
Nice to have
• brillant colors and artistic

```html
<!DOCTYPE html>
<html lang="en">
<head>
<meta charset="utf-8">
<title>Natural Honey by Morrow – Jar Label</title>
<link rel="stylesheet" href="https://fonts.googleapis.com/css2?family=Montserrat:wght@500;700;800&family=Dancing+Script:wght@500&display=swap">
<style>
  :root {
    --backdrop: #f2f1ee;
    --label-olive: #8b6c1f;
    --label-olive-dark: #7a5d17;
    --comb-dark: #3f2810;
    --comb-amber: #e3a526;
    --comb-gold: #f2c14a;
    --leaf-green: #9cc43a;
    --honey-white: #ffffff;
    --bar-brown: #3d2810;
    --script-cream: #f6ecd2;
  }
  * { margin: 0; padding: 0; box-sizing: border-box; }
  html, body {
    width: 800px;
    height: 1200px;
    overflow: hidden;
    background: var(--backdrop);
  }
  .canvas {
    position: relative;
    width: 800px;
    height: 1200px;
    display: flex;
    align-items: center;
    justify-content: center;
  }
  .honey-label {
    position: relative;
    width: 640px;
    height: 700px;
    background: linear-gradient(180deg, var(--label-olive) 0%, var(--label-olive-dark) 100%);
    overflow: hidden;
  }
  .comb-band {
    position: absolute;
    left: 0;
    top: 0;
    width: 100%;
    height: 300px;
    background:
      radial-gradient(ellipse at 70% 90%, var(--comb-gold) 0%, rgba(227,165,38,0) 45%),
      linear-gradient(180deg, var(--comb-dark) 0%, #5a3a14 55%, var(--comb-amber) 100%);
  }
  .brand-natural {
    position: absolute;
    left: 72px;
    top: 322px;
    font-family: "Montserrat", sans-serif;
    font-weight: 500;
    font-size: 44px;
    letter-spacing: 1px;
    color: var(--leaf-green);
  }
  .brand-honey {
    position: absolute;
    left: 66px;
    top: 368px;
    font-family: "Montserrat", sans-serif;
    font-weight: 800;
    font-size: 138px;
    line-height: 1;
    letter-spacing: 2px;
    color: var(--honey-white);
  }
  .brand-bar {
    position: absolute;
    left: 80px;
    top: 530px;
    width: 300px;
    height: 22px;
    background: var(--bar-brown);
  }
  .brand-maker {
    position: absolute;
    left: 400px;
    top: 536px;
    font-family: "Dancing Script", cursive;
    font-weight: 500;
    font-size: 46px;
    color: var(--script-cream);
  }
</style>
</head>
<body>
  <main class="canvas">
    <section class="honey-label" aria-label="Natural Honey by Morrow">
      <div class="comb-band" role="img" aria-label="Dark honeycomb pattern with golden honey dripping down"></div>
      <p class="brand-natural">NATURAL</p>
      <h1 class="brand-honey">HONEY</h1>
      <div class="brand-bar"></div>
      <p class="brand-maker">by Morrow</p>
    </section>
  </main>
</body>
</html>
```